New Alcoholic Spiked Seltzer Line

We need a can design for a line of low calorie alcoholic seltzer. This product is a sparkling water and vodka drink with no sugar added in a slim 12 oz can.

This is a lighter, healthier, alternative to the sugary ready-to-drinks on the market. The product contains only 3 ingredients: Vodka, Water and Natural Flavors. It has only 100 calories but still has 5% alcohol, so you don't need to sacrifice alcohol to cut calories.

This product also does not contain any preservatives.

We want this design to communicate the following objectives to the consumer and in this order:

1. Appetizing product
2.Low calorie
3.Communicate the type of beverage (Spiked Seltzer)

The brand name of the product is ZIVA.

The flavor of the product needed to be used for the design is Mango-Orange.

Comparable products are:

www.brightfizzcanhouse.example/
https://www.lumabubble.example
https://palefernco.example/

The designs should not infringe or copy the creative directions of the products mentionned above. They are only given so that you can better understand the type of product we are developing.

Target Market(s)

Young Professional women between the ages of 25 and 44

Industry/Entity Type

Product

Colors

Designer to choose colors to be used in the design.

Requirements
Must have
• Design extendibility, meaning it can be adapted for other flavors.
• This is a new category in the market we are targeting, so consumers must easily be able to identify what type of product this is.

```html
<!DOCTYPE html>
<html lang="en">
<head>
<meta charset="utf-8">
<title>ZIVA Spiked Seltzer – Mango Orange</title>
<link rel="stylesheet" href="https://fonts.googleapis.com/css2?family=Montserrat:wght@500&family=Source+Sans+3:wght@400;500;600&display=swap">
<style>
  :root {
    --silver-edge: #b9bbbe;
    --silver-mid: #e4e5e7;
    --silver-light: #f4f4f5;
    --wine: #7a0d14;
    --berry: #c41f45;
    --berry-bar: #b21c48;
    --slate: #3b3b3d;
    --charcoal: #333436;
    --band: #2c2d2f;
    --mango: #f5a100;
    --mango-deep: #e38d00;
    --mango-text: #f2a81d;
    --white: #ffffff;
  }
  * { margin: 0; padding: 0; box-sizing: border-box; }
  html, body { width: 1200px; height: 2546px; overflow: hidden; }
  body {
    font-family: "Source Sans 3", sans-serif;
    background: var(--silver-light);
  }
  .can-label {
    position: relative;
    width: 1200px;
    height: 2546px;
    overflow: hidden;
    background: linear-gradient(90deg, var(--silver-edge) 0%, var(--silver-mid) 18%, var(--silver-light) 45%, var(--silver-mid) 75%, var(--silver-edge) 100%);
  }
  .product-type {
    position: absolute;
    right: 630px;
    top: 490px;
    text-align: right;
    color: var(--wine);
    font-weight: 500;
    font-size: 96px;
    line-height: 1.02;
  }
  .tagline {
    position: absolute;
    right: 630px;
    top: 705px;
    text-align: right;
    color: var(--berry);
    font-size: 52px;
    line-height: 1.2;
  }
  .ingredients {
    position: absolute;
    right: 630px;
    top: 835px;
    text-align: right;
    color: var(--slate);
    font-size: 52px;
    line-height: 1.2;
  }
  .accent-bar {
    position: absolute;
    left: 255px;
    top: 962px;
    width: 315px;
    height: 52px;
    background: var(--berry-bar);
  }
  .emblem-art {
    position: absolute;
    left: 160px;
    top: 1040px;
    width: 505px;
    height: 320px;
  }
  .brand-name {
    position: absolute;
    left: 790px;
    top: 1250px;
    width: 1600px;
    transform: translate(-50%, -50%) rotate(-90deg);
    text-align: center;
    font-family: "Montserrat", sans-serif;
    font-weight: 500;
    font-size: 575px;
    line-height: 1;
    letter-spacing: 0.02em;
    color: var(--charcoal);
    white-space: nowrap;
  }
  .flavor-badge {
    position: absolute;
    left: 150px;
    top: 1540px;
    width: 420px;
    height: 420px;
  }
  .flavor-badge svg {
    position: absolute;
    inset: 0;
    width: 100%;
    height: 100%;
  }
  .flavor-name {
    position: absolute;
    inset: 0;
    display: flex;
    flex-direction: column;
    align-items: center;
    justify-content: center;
    color: var(--white);
    font-weight: 600;
    font-size: 104px;
    line-height: 0.95;
    transform: rotate(-8deg);
  }
  .info-band {
    position: absolute;
    left: 0;
    bottom: 0;
    width: 100%;
    height: 398px;
    background: var(--band);
  }
  .info-band p {
    position: absolute;
    top: 95px;
    width: 100%;
    text-align: center;
    color: var(--mango-text);
    font-size: 64px;
    font-weight: 500;
  }
</style>
</head>
<body>
  <main class="can-label">
    <h1 class="product-type">Spiked<br>Seltzer</h1>
    <p class="tagline">low calorie<br>alcoholic seltzer</p>
    <p class="ingredients">vodka, water &amp;<br>natural flavors</p>
    <div class="accent-bar"></div>

    <svg class="emblem-art" viewBox="0 0 505 320" role="img" aria-label="Line illustration of a ram's head with curled horns">
      <defs>
        <radialGradient id="emblem-tone" cx="50%" cy="50%" r="50%">
          <stop offset="0%" stop-color="#c9cacc"/>
          <stop offset="100%" stop-color="#c9cacc" stop-opacity="0"/>
        </radialGradient>
      </defs>
      <ellipse cx="252" cy="160" rx="250" ry="158" fill="url(#emblem-tone)"/>
    </svg>

    <div class="brand-name">ZIVA</div>

    <div class="flavor-badge">
      <svg viewBox="0 0 420 420" role="img" aria-label="Orange brush-textured circle">
        <defs>
          <linearGradient id="badge-tone" x1="0" y1="0" x2="1" y2="1">
            <stop offset="0%" stop-color="#f5a100"/>
            <stop offset="100%" stop-color="#e38d00"/>
          </linearGradient>
        </defs>
        <circle cx="210" cy="210" r="206" fill="url(#badge-tone)"/>
      </svg>
      <p class="flavor-name"><span>mango</span><span>orange</span></p>
    </div>

    <footer class="info-band">
      <p>5% alcohol - 100 calories</p>
    </footer>
  </main>
</body>
</html>
```